Professional New Resume for personal/ company

Specialist in construction law, disputes and quantity surveying. Looking for a new fresh CV to appeal to the middle east (UAE) market.

Target Market(s)

employers, clients, lawyers, expert witnesses

Industry/Entity Type

Construction law, quantity surveying, dispute resolution.

```html
<!DOCTYPE html>
<html lang="en">
<head>
<meta charset="utf-8">
<title>Marcus J Ellory – CV</title>
<link rel="stylesheet" href="https://fonts.googleapis.com/css2?family=Montserrat:wght@500;600;700;800&family=Open+Sans:wght@400;600&display=swap">
<style>
:root{
  --blue:#1f5fbf;
  --blue-light:#3a7bd5;
  --navy:#1f2431;
  --ink:#2a2d35;
  --muted:#5a5f6b;
  --white:#ffffff;
  --bg:#d6d6d6;
  --rule:#c9ced8;
}
*{box-sizing:border-box;margin:0;padding:0}
html,body{width:1200px;height:877px;overflow:hidden}
body{background:var(--bg);font-family:"Open Sans",Arial,sans-serif;color:var(--ink)}
.cv{position:absolute;left:303px;top:18px;width:594px;height:841px;background:var(--white);overflow:hidden;box-shadow:0 6px 22px rgba(0,0,0,.18)}
.top-band{position:absolute;left:0;top:0;width:100%;height:36px;background:var(--blue)}
.brand{position:absolute;left:0;top:36px;width:232px;height:70px;background:var(--blue);display:flex;align-items:center;padding-left:22px}
.brand-name{font-family:"Montserrat",sans-serif;font-weight:500;font-size:22px;letter-spacing:6px;color:var(--white)}
.portrait{position:absolute;left:0;top:106px;width:232px;height:186px;background:linear-gradient(180deg,#eef0f3 0%,#d9dde4 55%,#2c3140 100%)}
.overview{position:absolute;left:250px;top:50px;width:326px}
.section-title{font-family:"Montserrat",sans-serif;font-weight:700;font-size:16px;color:var(--blue);text-align:center;padding-bottom:6px;border-bottom:2px solid var(--blue);margin-bottom:12px}
.overview p{font-size:8.4px;line-height:1.55;color:var(--ink);margin-bottom:11px}
.name-band{position:absolute;left:0;top:292px;width:296px;height:86px;background:var(--blue-light);padding:14px 0 0 22px;color:var(--white)}
.name{font-family:"Montserrat",sans-serif;font-weight:800;font-size:22px;letter-spacing:.3px;text-transform:uppercase}
.credentials{font-family:"Montserrat",sans-serif;font-weight:500;font-size:12px;line-height:1.35;margin-top:3px}
.contact{position:absolute;left:300px;top:252px;width:286px;height:82px;display:flex}
.contact-icons{width:22px;background:var(--navy);display:flex;flex-direction:column;justify-content:space-around;align-items:center;padding:8px 0}
.contact-list{list-style:none;padding:8px 10px;font-size:8.6px;line-height:1.4;color:var(--ink)}
.contact-list li{margin-bottom:2px}
.sidebar{position:absolute;left:0;top:378px;width:268px;height:463px;background:var(--navy)}
.card{position:absolute;left:22px;width:222px;background:var(--white);border-radius:8px;padding:26px 14px 12px 14px}
.card-qual{top:412px}
.card-memb{top:570px}
.pill{position:absolute;font-family:"Montserrat",sans-serif;font-weight:700;font-size:10.5px;color:var(--white);background:var(--blue);border-radius:10px;padding:5px 18px}
.card .pill{left:-6px;top:-10px;width:190px}
.card ul{padding-left:14px;font-size:8.4px;line-height:1.45;color:var(--ink)}
.card li{margin-bottom:7px}
.experience{position:absolute;left:286px;top:345px;width:290px}
.experience .pill{position:relative;display:block;width:150px;margin-left:-4px;margin-bottom:12px}
.timeline{position:relative;padding-left:16px;border-left:1.5px dotted var(--rule);margin-left:2px}
.job{position:relative;display:grid;grid-template-columns:44px 1fr;column-gap:8px;row-gap:2px;font-size:8.4px;line-height:1.4;margin-bottom:16px}
.job::before{content:"";position:absolute;left:-20.5px;top:3px;width:7px;height:7px;border-radius:50%;background:var(--blue)}
.job dt{font-weight:600;color:var(--muted)}
.job dd{color:var(--ink)}
</style>
</head>
<body>
<article class="cv">
  <div class="top-band"></div>

  <header class="brand"><span class="brand-name">KALDEN</span></header>
  <div class="portrait" role="img" aria-label="Portrait photograph of Marcus J Ellory in a pinstripe suit and tie"></div>

  <section class="overview">
    <h2 class="section-title">Overview</h2>
    <p>Adjudicator, Chartered Quantity Surveyor and Chartered Construction Manager with experience in Private Practice, Development and Main Contracting industry. Claims, contract and dispute resolution (adjudication) services as adjudicator or party representative provided in Scotland, England and Wales.</p>
    <p>Qualifications include: a BSc (Hons) in Quantity Surveying, LLM Masters of Laws (Construction Law), Fellow of the Institute of Arbitration Practitioners (FIAP), Fellow of the Royal Guild of Chartered Surveyors (FRGCS), Member of the Institute of Civil Engineering Surveyors (MICES) and a Professional Member of the Institute of Building Professionals (MIBP). Experience includes involvement in a large and complex international arbitration. Experienced in standard UK and international contract forms.</p>
  </section>

  <section class="name-band">
    <h1 class="name">Marcus J Ellory</h1>
    <p class="credentials">BSc (Hons), Dip. Adj, LLM, FIAP,<br>FRGCS, MICES, MIBP</p>
  </section>

  <aside class="contact">
    <div class="contact-icons">
      <svg width="9" height="9" viewBox="0 0 24 24" aria-hidden="true"><path fill="#fff" d="M6.6 10.8a15.1 15.1 0 0 0 6.6 6.6l2.2-2.2c.3-.3.7-.4 1-.2 1.1.4 2.3.6 3.6.6.6 0 1 .4 1 1V20c0 .6-.4 1-1 1A17 17 0 0 1 3 4c0-.6.4-1 1-1h3.5c.6 0 1 .4 1 1 0 1.3.2 2.5.6 3.6.1.3 0 .7-.2 1z"/></svg>
      <svg width="9" height="9" viewBox="0 0 24 24" aria-hidden="true"><path fill="#fff" d="M2 5h20v14H2zm2 2v.5l8 5 8-5V7l-8 5z"/></svg>
      <svg width="9" height="9" viewBox="0 0 24 24" aria-hidden="true"><path fill="#fff" d="M12 2a7 7 0 0 0-7 7c0 5 7 13 7 13s7-8 7-13a7 7 0 0 0-7-7zm0 9.5A2.5 2.5 0 1 1 12 6.5a2.5 2.5 0 0 1 0 5z"/></svg>
    </div>
    <ul class="contact-list">
      <li>+44 (0)7000 123 456</li>
      <li>mellory@kaldenqs.com</li>
      <li>2nd Floor, 18 Harlow Crescent,<br>Brackenford, United Kingdom, BF3 7QT</li>
    </ul>
  </aside>

  <div class="sidebar"></div>

  <section class="card card-qual">
    <h3 class="pill">Qualifications</h3>
    <ul>
      <li>BSc (Hons) Quantity Surveying (Northbridge University) (part time)</li>
      <li>LLM Masters of Law (Construction Law) (University of Westmoor) (with Merit)</li>
      <li>Diploma in Adjudication (IAP)</li>
    </ul>
  </section>

  <section class="card card-memb">
    <h3 class="pill">Memberships</h3>
    <ul>
      <li>Fellow of the Institute of Arbitration Practitioners</li>
      <li>Fellow of the Royal Guild of Chartered Surveyors</li>
      <li>Member of the Institute of Civil Engineering Surveyors</li>
      <li>Member of the Institute of Building Professionals</li>
      <li>Adjudicator &amp; Panel Member – APG (Adjudication Panel Group)</li>
    </ul>
  </section>

  <section class="experience">
    <h3 class="pill">Experience</h3>
    <div class="timeline">
      <dl class="job">
        <dt>Project:</dt><dd>Confidential</dd>
        <dt>Value:</dt><dd>£12bn claim &amp; counter-claim</dd>
        <dt>For:</dt><dd>Parties to an International Arbitration</dd>
        <dt>Date:</dt><dd>December 2021 to Current</dd>
        <dt>Services:</dt><dd>Tribunal Secretary to assist the Arbitral Tribunal (Chairman Helen Marsh KC) and two co-arbitrators (Sir Owen Blake and David Renner KC).</dd>
      </dl>
      <dl class="job">
        <dt>Project:</dt><dd>Various</dd>
        <dt>Value:</dt><dd>Various</dd>
        <dt>For:</dt><dd>Adjudicator in Construction Disputes, nominated by Adjudication Panel Group</dd>
        <dt>Date:</dt><dd>October 2021 to current</dd>
        <dt>Services:</dt><dd>Adjudicator</dd>
      </dl>
      <dl class="job">
        <dt>Project:</dt><dd>Flat Development, Brackenford</dd>
        <dt>Value:</dt><dd>£24,000</dd>
        <dt>For:</dt><dd>Referring Party (Contractor)</dd>
        <dt>Date:</dt><dd>December 2020</dd>
        <dt>Services:</dt><dd>Representative for Referring Party</dd>
      </dl>
      <dl class="job">
        <dt>Project:</dt><dd>Supermarkets (Various)</dd>
        <dt>Value:</dt><dd>Various</dd>
        <dt>For:</dt><dd>Referring Party (Subcontractor)</dd>
        <dt>Date:</dt><dd>January 2019</dd>
        <dt>Services:</dt><dd>Representative for Referring Party</dd>
      </dl>
    </div>
  </section>
</article>
</body>
</html>
```